Technology Consulting
I need single sided standard sized Business Card [3.5" x 2"]
use something that looks conservative and contemporary
Simple
Mark Delaney
System's Engineer
48 Harrow Lane
mdelaney@quorvalenconsulting.com
http://www.quorvalenconsutling.com
use a font that looks conservative and contemporary

```html
<!DOCTYPE html>
<html lang="en">
<head>
<meta charset="utf-8">
<title>Quorvalen Consulting – Business Cards</title>
<link href="https://fonts.googleapis.com/css2?family=Open+Sans:wght@400;600;700&display=swap" rel="stylesheet">
<style>
  :root {
    --page-bg: #e9e6e1;
    --card-white: #ffffff;
    --card-grey: #f1f1f3;
    --navy: #0d2f63;
    --navy-deep: #061a3e;
    --blue: #1f5fae;
    --blue-bright: #2f86d3;
    --text-dark: #333a44;
    --logo-blue: #1c4c8c;
  }
  * { box-sizing: border-box; margin: 0; padding: 0; }
  html, body { width: 1200px; height: 739px; overflow: hidden; }
  body {
    background: var(--page-bg);
    font-family: "Open Sans", Arial, sans-serif;
    position: relative;
  }
  .card {
    position: absolute;
    width: 460px;
    height: 286px;
    border-radius: 24px;
    overflow: hidden;
    box-shadow: 0 3px 8px rgba(0,0,0,0.25);
  }
  .card--front { left: 96px; top: 66px; background: linear-gradient(180deg, var(--card-white) 0%, var(--card-grey) 100%); }
  .card--back-light { left: 644px; top: 66px; background: linear-gradient(180deg, var(--card-white) 0%, var(--card-grey) 100%); }
  .card--back-dark { left: 96px; top: 390px; background: radial-gradient(ellipse at 50% 45%, var(--blue-bright) 0%, var(--blue) 35%, var(--navy) 75%, var(--navy-deep) 100%); }
  .card--back-glow { left: 644px; top: 390px; background: radial-gradient(ellipse at 35% 40%, var(--blue-bright) 0%, var(--blue) 40%, var(--navy) 80%, var(--navy-deep) 100%); }

  .name-tab {
    position: absolute; right: 0; top: 24px;
    width: 150px; height: 50px;
    background: linear-gradient(180deg, var(--blue) 0%, var(--navy) 100%);
    border-radius: 8px 0 0 8px;
    color: #fff; text-align: center;
    padding-top: 7px;
  }
  .name-tab__name { font-size: 15px; font-weight: 600; }
  .name-tab__title { font-size: 10px; opacity: 0.9; }

  .brand { display: flex; align-items: center; gap: 10px; color: var(--logo-blue); font-weight: 700; }
  .brand__dot { border-radius: 50%; background: var(--logo-blue); flex: none; }
  .brand--front { position: absolute; left: 22px; top: 110px; font-size: 38px; letter-spacing: 1px; }
  .brand--front .brand__dot { width: 40px; height: 40px; }
  .brand--center { position: absolute; left: 0; right: 0; justify-content: center; font-size: 24px; }
  .brand--center .brand__dot { width: 30px; height: 30px; }
  .brand--light { color: #fff; }
  .brand--light .brand__dot { background: #fff; }
  .brand--faint { color: rgba(255,255,255,0.75); }
  .brand--faint .brand__dot { background: rgba(255,255,255,0.75); }

  .contact-list {
    position: absolute; right: 16px; top: 196px;
    text-align: right; font-size: 11px; line-height: 16px; color: var(--text-dark);
  }
  .address { position: absolute; left: 22px; top: 228px; font-size: 11px; color: var(--text-dark); }

  .url-bar {
    position: absolute; left: 50%; transform: translateX(-50%);
    font-size: 11px; padding: 5px 18px; border-radius: 3px;
  }
  .url-bar--navy { top: 204px; background: linear-gradient(180deg, var(--blue) 0%, var(--navy) 100%); color: #fff; width: 230px; text-align: center; }
  .url-bar--white { top: 200px; background: #fff; color: var(--text-dark); width: 280px; text-align: left; box-shadow: 0 1px 3px rgba(0,0,0,0.4); }
  .url-plain { position: absolute; left: 30px; bottom: 24px; font-size: 11px; color: #fff; }
</style>
</head>
<body>

<section class="card card--front">
  <div class="name-tab">
    <p class="name-tab__name">Mark Delaney</p>
    <p class="name-tab__title">System's Engineer</p>
  </div>
  <div class="brand brand--front"><span class="brand__dot"></span>Quorvalen</div>
  <div class="contact-list">
    <p>281.555.0147 : P</p>
    <p>713.555.0193 : C</p>
    <p>mdelaney@quorvalenconsulting.com : E</p>
    <p>www.quorvalenconsulting.com</p>
  </div>
  <p class="address">48 Harrow Lane</p>
</section>

<section class="card card--back-light">
  <div class="brand brand--center" style="top:146px;"><span class="brand__dot"></span>Quorvalen</div>
  <p class="url-bar url-bar--navy">www.quorvalenconsulting.com</p>
</section>

<section class="card card--back-dark">
  <div class="brand brand--center brand--faint" style="top:140px;"><span class="brand__dot"></span>Quorvalen</div>
  <p class="url-bar url-bar--white">www.quorvalenconsulting.com</p>
</section>

<section class="card card--back-glow">
  <div class="brand brand--center brand--light" style="top:196px;"><span class="brand__dot"></span>Quorvalen</div>
  <p class="url-plain">www.quorvalenconsulting.com</p>
</section>

</body>
</html>
```